Re-branding for Structural Engineering firm

We need new business cards as part of our current re-branding. We have a new logo (attached), so the card design should incorporate this color scheme. We are a structural engineering firm providing structural building design and seismic consulting services. The final design should communicate professionalism and stability, with a modern look and feel.

```html
<!DOCTYPE html>
<html lang="en">
<head>
<meta charset="utf-8">
<title>Halvard Structural Engineering – Business Card</title>
<link rel="stylesheet" href="https://fonts.googleapis.com/css2?family=Roboto:wght@400;500;700&family=Lato:wght@700&display=swap">
<style>
  :root {
    --brand-blue: #1272b8;
    --brand-blue-soft: #2a83c4;
    --brand-gray: #7d7d7d;
    --ink: #3a3a3a;
    --rule: #4a4a4a;
    --paper: #fbfbfb;
    --backdrop: #e6e6e6;
    --white: #ffffff;
  }
  * { margin: 0; padding: 0; box-sizing: border-box; }
  html, body { width: 1200px; height: 960px; overflow: hidden; }
  body { background: var(--backdrop); font-family: "Roboto", Arial, sans-serif; position: relative; }

  .card { position: absolute; overflow: hidden; }
  .card--front { left: 314px; top: 113px; width: 602px; height: 343px; background: var(--paper); }
  .card--back { left: 311px; top: 472px; width: 600px; height: 343px; background: var(--brand-blue); }

  /* front: brand name */
  .brand { position: absolute; right: 36px; top: 30px; text-align: right; }
  .brand__mark { display: block; width: 42px; height: 42px; background: var(--brand-blue); margin: 0 0 14px auto; }
  .brand__name { font-family: "Lato", sans-serif; font-weight: 700; color: var(--brand-blue); font-size: 18px; line-height: 19px; letter-spacing: 0.2px; }

  .accent-bar { position: absolute; left: 0; top: 169px; width: 14px; height: 38px; background: var(--brand-blue); }
  .person { position: absolute; left: 34px; top: 166px; }
  .person__name { font-weight: 500; font-size: 21px; color: var(--brand-blue); letter-spacing: 0.3px; }
  .person__title { font-size: 15px; color: var(--brand-gray); letter-spacing: 0.8px; margin-top: 3px; }

  .divider { position: absolute; left: 34px; top: 219px; width: 532px; height: 1px; background: var(--rule); }

  .contact { position: absolute; left: 34px; top: 235px; list-style: none; font-size: 14.5px; color: var(--ink); }
  .contact li { display: flex; align-items: center; height: 19.5px; }
  .contact svg { width: 14px; height: 14px; margin-right: 8px; fill: var(--brand-blue); }

  .address { position: absolute; right: 36px; top: 256px; text-align: right; font-size: 14.5px; line-height: 19px; color: var(--ink); font-style: normal; }

  .footer-band { position: absolute; left: 0; top: 312px; width: 602px; height: 31px; }
  .footer-url { position: absolute; right: 44px; top: 318px; font-size: 14px; letter-spacing: 2.6px; color: var(--white); }

  /* back */
  .back-panel { position: absolute; left: 25px; top: 22px; width: 298px; height: 297px; background: var(--brand-blue-soft); opacity: 0.7; }
  .back-title { position: absolute; right: 38px; top: 238px; text-align: right; font-family: "Lato", sans-serif; font-weight: 700; font-size: 30px; line-height: 29px; color: var(--white); }
  .back-url { position: absolute; right: 38px; top: 303px; font-size: 14px; letter-spacing: 3px; color: var(--white); }
</style>
</head>
<body>

<section class="card card--front">
  <div class="brand">
    <span class="brand__mark"></span>
    <div class="brand__name">HALVARD<br>STRUCTURAL<br>ENGINEERING</div>
  </div>

  <span class="accent-bar"></span>
  <div class="person">
    <div class="person__name">CAL RENNER, S.E.</div>
    <div class="person__title">PRINCIPAL</div>
  </div>

  <span class="divider"></span>

  <ul class="contact">
    <li><svg viewBox="0 0 24 24"><path d="M6.6 10.8a15 15 0 0 0 6.6 6.6l2.2-2.2a1 1 0 0 1 1-.25 11.4 11.4 0 0 0 3.6.57 1 1 0 0 1 1 1V20a1 1 0 0 1-1 1A17 17 0 0 1 3 4a1 1 0 0 1 1-1h3.5a1 1 0 0 1 1 1c0 1.25.2 2.45.57 3.57a1 1 0 0 1-.25 1z"/></svg>858.555.0143</li>
    <li><svg viewBox="0 0 24 24"><path d="M7 1h10a2 2 0 0 1 2 2v18a2 2 0 0 1-2 2H7a2 2 0 0 1-2-2V3a2 2 0 0 1 2-2zm0 3v14h10V4zm5 15.2a1.1 1.1 0 1 0 0 2.2 1.1 1.1 0 0 0 0-2.2z"/></svg>619.555.0187</li>
    <li><svg viewBox="0 0 24 24"><path d="M2 5h20v14H2zm2 2v.5l8 5 8-5V7zm0 2.9V17h16V9.9l-8 5z"/></svg>cal@halvardse.com</li>
  </ul>

  <address class="address">4170 Alder Ridge Rd., Ste. 210<br>San Diego, California 92108</address>

  <svg class="footer-band" viewBox="0 0 602 31" aria-hidden="true">
    <polygon points="354,0 583,0 583,31 0,31 0,25 338,25" fill="var(--brand-blue)"/>
    <rect x="585" y="0" width="17" height="31" fill="var(--brand-gray)"/>
  </svg>
  <div class="footer-url">www.halvardse.com</div>
</section>

<section class="card card--back">
  <span class="back-panel"></span>
  <div class="back-title">STRUCTURAL<br>ENGINEERING</div>
  <div class="back-url">www.halvardse.com</div>
</section>

</body>
</html>
```